Business card design for Allied Healthcare provider

We would like a design for front and back of business cards. The design must resonate with all levels of customers from patients, to other health providers and medical. Must also resonate with corporate customers

Target Market(s)

patients, medical practitioners, other health providers and corporate.

Industry/Entity Type

healthcare

Contact Information for Business Card

name, logo, phone and fax numbers, email, website

Requirements
Must have
• not allowing me to change this, but the card must be double sided!! Please take note
Nice to have
• a fresh yet bold design to catch attention.

```html
<!DOCTYPE html>
<html lang="en">
<head>
<meta charset="utf-8">
<title>Nuvaleth Business Card — Front and Back</title>
<link rel="stylesheet" href="https://fonts.googleapis.com/css2?family=Montserrat:wght@600;700;800&family=Open+Sans:wght@400;600&display=swap">
<style>
  :root {
    --navy: #1a2b58;
    --navy-light: #243a72;
    --gold: #fbb62a;
    --white: #ffffff;
    --grey-text: #5b5f69;
    --stage: #d9d9d6;
  }
  * { box-sizing: border-box; margin: 0; padding: 0; }
  html, body { width: 1200px; height: 801px; overflow: hidden; }
  body {
    background: var(--stage);
    position: relative;
    font-family: "Open Sans", sans-serif;
  }
  .card {
    position: absolute;
    top: 252px;
    width: 520px;
    height: 297px;
    border-radius: 18px;
    overflow: hidden;
    box-shadow: 0 6px 18px rgba(0,0,0,0.18);
  }
  .card-front { left: 50px; background: var(--white); }
  .card-back  { left: 630px; background: var(--navy); }

  /* Front */
  .brand {
    position: absolute; left: 34px; top: 46px;
    display: flex; align-items: center; gap: 10px;
  }
  .brand-dot { width: 14px; height: 14px; border-radius: 50%; background: var(--gold); flex: none; }
  .brand-name {
    font-family: "Montserrat", sans-serif; font-weight: 800;
    font-size: 32px; color: var(--navy); letter-spacing: -0.5px; line-height: 1;
  }
  .tagline {
    position: absolute; left: 58px; top: 86px;
    font-family: "Montserrat", sans-serif; font-weight: 600;
    font-size: 12px; color: var(--gold); letter-spacing: 0.3px;
  }
  .person { position: absolute; left: 34px; top: 130px; }
  .person-name {
    font-family: "Montserrat", sans-serif; font-weight: 800;
    font-size: 19px; color: var(--navy); letter-spacing: 0.5px; text-transform: uppercase;
  }
  .person-title { font-size: 14px; color: var(--grey-text); margin-top: 2px; }
  .contacts {
    position: absolute; left: 34px; top: 196px;
    list-style: none; font-size: 13px; color: var(--grey-text); line-height: 21px;
  }
  .contacts li { display: flex; align-items: center; gap: 8px; }
  .contacts svg { width: 11px; height: 11px; fill: var(--gold); flex: none; }

  .feature-mark {
    position: absolute; left: 300px; right: 24px; top: 0; bottom: 0;
    display: flex; align-items: center; justify-content: center;
  }
  .feature-name {
    font-family: "Montserrat", sans-serif; font-weight: 800;
    font-size: 44px; color: var(--navy); letter-spacing: -1px; line-height: 1;
  }

  /* Back */
  .back-brand {
    position: absolute; left: 0; right: 0; top: 0; bottom: 0;
    display: flex; align-items: center; justify-content: center; gap: 14px;
  }
  .back-dot { width: 20px; height: 20px; border-radius: 50%; background: var(--navy-light); }
  .back-name {
    font-family: "Montserrat", sans-serif; font-weight: 800;
    font-size: 56px; color: var(--navy-light); letter-spacing: -1px;
  }
</style>
</head>
<body>

<section class="card card-front" aria-label="Card front">
  <div class="brand">
    <span class="brand-dot"></span>
    <span class="brand-name">nuvaleth</span>
  </div>
  <div class="tagline">guidance · care · wellness</div>

  <div class="person">
    <div class="person-name">Daniel Reyes</div>
    <div class="person-title">President</div>
  </div>

  <ul class="contacts">
    <li><svg viewBox="0 0 10 10"><path d="M2 0h2l1 2.5-1.3 1a5 5 0 0 0 2.8 2.8l1-1.3L10 6v2a2 2 0 0 1-2 2A8 8 0 0 1 0 2 2 2 0 0 1 2 0z"/></svg>555-014-2290</li>
    <li><svg viewBox="0 0 10 10"><rect x="2" y="0" width="6" height="3"/><rect x="0" y="3.5" width="10" height="4.5" rx="1"/><rect x="2" y="7" width="6" height="3"/></svg>555-014-2291</li>
    <li><svg viewBox="0 0 10 10"><path d="M0 2h10v6H0z M0 2l5 3.5L10 2"/></svg>info@nuvaleth-group.com</li>
    <li><svg viewBox="0 0 10 10"><circle cx="5" cy="5" r="5"/></svg>www.nuvaleth-group.com</li>
  </ul>

  <div class="feature-mark">
    <span class="feature-name">nuvaleth</span>
  </div>
</section>

<section class="card card-back" aria-label="Card back">
  <div class="back-brand">
    <span class="back-dot"></span>
    <span class="back-name">nuvaleth</span>
  </div>
</section>

</body>
</html>
```